Technology Project Portal - Project Listing portal

We require a logo & website designed for our new project.

Project Name: lumafold
Description:
We have a webapp where clients and service providers can come, signup and register development projects. Service providers can the browse projects and contact clients via the portal

Design brief:
Clean & Modern - See Attached color palet & style references. (Feel free to try alternative color palets)

See Project Proposal for site requirements.
UX flow section details pages requires

Examples of all standard UI Components required e.g.
text box / field
Drop down
date picker
etc..

Target Market(s)

Business / Technology providers

Logo Text

LumaFold

Coding

Coded - Design and coding required

Number of Pages Required

5+ page

Requirements
Must have
• Clean Modern Design
Examples for all common UI elements
Templates for common Web App Dialogs e.g. Confirm Delete/Logout etc

```html
<!DOCTYPE html>
<html lang="en">
<head>
<meta charset="utf-8">
<title>LumaFold – Portal Screens</title>
<link href="https://fonts.googleapis.com/css2?family=Montserrat:wght@400;500;700;800&family=Roboto:wght@500;700&display=swap" rel="stylesheet">
<style>
  :root{
    --page:#f5f5f5;
    --red:#fa2a0c;
    --red-deep:#8a1a0c;
    --red-dark:#3a0f0a;
    --panel-grey:#6d6c71;
    --field-line:#e6e6e8;
    --white:#ffffff;
    --ink:#1a1a1a;
    --photo-dark:#05080f;
    --photo-blue:#24405e;
  }
  *{box-sizing:border-box;margin:0;padding:0}
  html,body{width:710px;height:1200px;overflow:hidden;background:var(--page)}
  body{position:relative;font-family:'Montserrat',sans-serif;color:var(--white)}

  .brand{font-family:'Montserrat',sans-serif;font-weight:800;color:var(--white);letter-spacing:-0.5px;line-height:1}

  /* Hero screen */
  .hero{position:absolute;left:119px;top:55px;width:470px;height:300px;overflow:hidden;
    background:radial-gradient(ellipse at 40% 35%,#a52a12 0%,var(--red-deep) 45%,var(--red-dark) 100%)}
  .hero .brand{position:absolute;left:9px;top:23px;font-size:25px}
  .btn-login{position:absolute;right:7px;top:22px;width:72px;height:25px;border-radius:13px;
    background:#111;border:1.5px solid var(--red);font-family:'Roboto',sans-serif;font-weight:700;
    font-size:9px;display:flex;align-items:center;justify-content:center;gap:4px}
  .hero-title{position:absolute;left:0;right:0;top:108px;text-align:center;font-family:'Montserrat',sans-serif;
    font-weight:800;font-size:30px;letter-spacing:0.5px}
  .hero-title .accent{color:var(--red)}
  .hero-text{position:absolute;left:22px;right:22px;top:160px;text-align:center;font-size:8px;line-height:14px;font-weight:500}
  .btn{position:absolute;height:25px;width:101px;border-radius:13px;background:var(--red);
    font-family:'Roboto',sans-serif;font-weight:700;font-size:11px;display:flex;align-items:center;justify-content:center;gap:6px;color:var(--white)}
  .hero .btn{left:185px;top:232px}

  /* Form panels */
  .panel{position:absolute;left:55px;width:600px;height:318px;display:flex;box-shadow:0 8px 22px rgba(0,0,0,0.25)}
  .panel-signup{top:457px}
  .panel-plan{top:828px}
  .panel-brand{width:200px;height:100%;position:relative;
    background:linear-gradient(160deg,#c8300f 0%,#a92510 50%,#8c1c0c 100%)}
  .panel-brand .brand{position:absolute;left:0;right:0;top:143px;text-align:center;font-size:34px}
  .panel-form{width:200px;height:100%;position:relative;background:var(--panel-grey)}
  .panel-photo{width:200px;height:100%;
    background:radial-gradient(ellipse at 55% 55%,var(--photo-blue) 0%,#142236 45%,var(--photo-dark) 85%)}

  .tab{position:absolute;top:50px;width:81px;height:25px;border-radius:13px;font-family:'Roboto',sans-serif;
    font-weight:700;font-size:11px;display:flex;align-items:center;justify-content:center}
  .tab-client{left:15px;border:1.5px solid var(--red);color:var(--red)}
  .tab-service{left:104px;background:var(--white);color:var(--panel-grey)}

  .field{position:absolute;left:16px;width:168px;height:27px;border:1px solid var(--field-line);
    display:flex;align-items:center;justify-content:space-between;padding:0 12px;font-size:8px}
  .panel-plan .field{left:18px;width:163px}

  .panel-form .btn{left:50px}
  .intro-image{position:absolute;left:15px;top:14px;width:171px;height:106px;
    background:linear-gradient(120deg,#1d2a3a 0%,#4a5462 45%,#c9b8a8 75%,#e8e2dc 100%)}
  .intro-text{position:absolute;left:19px;right:14px;top:129px;font-size:7.2px;line-height:12px}
</style>
</head>
<body>

<section class="hero">
  <div class="brand">LumaFold</div>
  <div class="btn-login">
    <svg width="7" height="8" viewBox="0 0 14 16"><circle cx="7" cy="4" r="4" fill="#fff"/><path d="M0 16c0-5 3-7 7-7s7 2 7 7z" fill="#fff"/></svg>
    LOGIN
  </div>
  <h1 class="hero-title">WELCOME TO <span class="accent">LUMAFOLD</span></h1>
  <p class="hero-text">Lorem ipsum dolor sit amet, consectetur adipiscing elit, sed do eiusmod tempor incididunt ut labore et dolore magna aliquauis ipsum suspendisse ultrices gravisus commodo viverra maecenas accumsan lacus vel facilisis. Lorem ipsum dolor sit amet, consectetur adipiscing elit, sed do eiusmod tempor incididunt ut labore et dolore magna aliquauis ipsum suspendisse ultrices gravisus commodo viverra maecenas</p>
  <div class="btn">
    <svg width="11" height="10" viewBox="0 0 22 20" fill="none" stroke="#fff" stroke-width="2"><rect x="1" y="4" width="14" height="14" rx="2"/><path d="M9 12l10-10 2 2-10 10H9z"/></svg>
    SIGN UP
  </div>
</section>

<section class="panel panel-signup">
  <div class="panel-brand"><div class="brand">LumaFold</div></div>
  <div class="panel-form">
    <div class="tab tab-client">CLIENT</div>
    <div class="tab tab-service">SERVICE</div>
    <div class="field" style="top:102px"><span>Enter Name</span>
      <svg width="6" height="7" viewBox="0 0 14 16"><circle cx="7" cy="4" r="4" fill="#fff"/><path d="M0 16c0-5 3-7 7-7s7 2 7 7z" fill="#fff"/></svg></div>
    <div class="field" style="top:142px"><span>Enter Email</span>
      <svg width="8" height="6" viewBox="0 0 16 12"><rect width="16" height="12" rx="1" fill="#fff"/><path d="M0 1l8 6 8-6" stroke="#6d6c71" stroke-width="1.5" fill="none"/></svg></div>
    <div class="field" style="top:182px"><span>Password</span>
      <svg width="8" height="7" viewBox="0 0 16 14"><rect x="0" y="6" width="10" height="8" rx="1" fill="#fff"/><path d="M7 6V4a4 4 0 0 1 8 0v1" stroke="#fff" stroke-width="2" fill="none"/></svg></div>
    <div class="btn" style="top:243px">
      <svg width="10" height="10" viewBox="0 0 20 20"><circle cx="10" cy="10" r="10" fill="#fff"/><path d="M5 10h8M10 6l4 4-4 4" stroke="#fa2a0c" stroke-width="2.4" fill="none"/></svg>
      NEXT
    </div>
  </div>
  <div class="panel-photo" role="img" aria-label="Photo of a developer working at a laptop at night, lit by projected code"></div>
</section>

<section class="panel panel-plan">
  <div class="panel-brand"><div class="brand">LumaFold</div></div>
  <div class="panel-form">
    <div class="intro-image" role="img" aria-label="Photo of hands typing on a laptop with code on screen"></div>
    <p class="intro-text">Lorem ipsum dolor sit amet, consectetur adipiscing elit, sed do eiusmod tempor incididunt ut labore et dolore magna aliqua. Quis ipsum suspendisse ultrices gravida.</p>
    <div class="field" style="top:194px"><span>Free/Low cost</span>
      <svg width="6" height="9" viewBox="0 0 12 18"><path d="M10 4C9 2 3 1.5 2.5 5s9 2.5 8 7-8 3-9 1M6 0v18" stroke="#fff" stroke-width="2" fill="none"/></svg></div>
    <div class="field" style="top:234px"><span>Paid / Pro-active</span>
      <svg width="9" height="8" viewBox="0 0 18 16"><path d="M0 1v6l8 8 7-7-8-8H1z" fill="#fff"/><circle cx="4" cy="4" r="1.5" fill="#6d6c71"/><path d="M10 0l8 8-7 7" stroke="#fff" stroke-width="1.6" fill="none"/></svg></div>
    <div class="btn" style="top:275px">
      <svg width="9" height="11" viewBox="0 0 14 18"><path d="M0 0h9l5 5v13H0z" fill="#fff"/><path d="M3 9h8M3 12h8M3 15h8" stroke="#fa2a0c" stroke-width="1.4"/></svg>
      SAVE
    </div>
  </div>
  <div class="panel-photo" role="img" aria-label="Photo of a developer working at a laptop at night, lit by projected code"></div>
</section>

</body>
</html>
```